Used Semi Truck Website Redesign

We are redoing the website backend and would like to also do a front end redesign. I would like a Mobile and Desktop mockup for each page. The website has more mobile visitors than desktop visitors. Our competitor is http://www.haulmarketbay.example. We don't want to copy them exactly but we want a site that looks more like that. We need the functionality of that site. One big difference is that we also sell parts and trailers.

We need a redesign for front page, product detail page, search result page, content page. It is very important that the site is very easy to use on mobile devices. Our target audience is Truck drivers.

Feel free to use demo fonts stock images, and icons. We will purchase necessary 3rd party media when a winner is chosen.

Target Market(s)

People who want to buy used trucks.

Coding

Coded - Design and coding required

Number of Pages Required

5+ page

Requirements
Must have
• Mockup for Desktop and Mobile pages.

```html
<!DOCTYPE html>
<html lang="en">
<head>
<meta charset="utf-8">
<title>Haulway Trucks</title>
<link href="https://fonts.googleapis.com/css2?family=Open+Sans:wght@400;600;700&family=Roboto+Slab:wght@400;700&display=swap" rel="stylesheet">
<style>
:root{
  --blue:#2d5596;
  --blue-dark:#1f3f73;
  --orange:#cc5a12;
  --ink:#2b2b2b;
  --text:#555;
  --muted:#888;
  --line:#e2e2e2;
  --band:#f5f5f5;
  --white:#fff;
}
*{box-sizing:border-box;margin:0;padding:0}
html,body{width:1200px;height:2490px;overflow:hidden}
body{font-family:"Open Sans",Arial,sans-serif;color:var(--text);background:var(--white);position:relative;font-size:12px}
a{color:inherit;text-decoration:none}
.site-header{height:108px;border-top:4px solid var(--blue);display:flex;align-items:center;padding:0 133px;justify-content:space-between}
.brand{font-family:"Roboto Slab",Georgia,serif;font-size:30px;color:var(--blue-dark);font-weight:400}
.top-nav{display:flex;align-items:center;gap:10px;font-size:12px;color:#444}
.top-nav .sep{color:#999}
.btn{display:inline-flex;align-items:center;gap:6px;color:var(--white);font-size:12px;padding:0 12px;height:32px;border-radius:2px}
.btn-orange{background:var(--orange)}
.btn-blue{background:var(--blue)}
.menu-toggle{display:flex;align-items:center;gap:8px;margin-left:6px;font-size:12px}
.menu-toggle .ring{width:40px;height:40px;border:1px solid #bbb;border-radius:50%;display:flex;align-items:center;justify-content:center}
.hero{position:absolute;top:108px;left:0;width:1200px;height:495px;background:linear-gradient(180deg,#5e7fa8 0%,#8ea4bf 38%,#b9bcbf 55%,#8f8f8d 100%)}
.hero-caption{position:absolute;left:619px;top:166px;width:448px;height:161px;background:rgba(30,30,30,.72);color:var(--white);text-align:center;padding-top:20px}
.hero-caption h1{font-family:"Roboto Slab",Georgia,serif;font-size:44px;font-weight:400;line-height:1.1}
.hero-caption h1 b{font-weight:700}
.hero-caption p{font-size:15px;line-height:1.5;margin-top:8px;padding:0 30px}
.hero-dots{position:absolute;left:1007px;top:360px;display:flex;gap:12px}
.hero-dots span{width:11px;height:11px;border-radius:50%;background:var(--white)}
.hero-dots span.on{background:var(--blue)}
.quick-search{position:absolute;top:603px;left:0;width:1200px;height:91px;background:#f1f1f1;display:flex;align-items:center;padding-left:133px;gap:10px}
.quick-search label{font-weight:700;color:var(--ink);font-size:13px;margin-right:2px}
.select{width:166px;height:28px;border:1px solid #ccc;background:var(--white);font-size:9px;color:#666;display:flex;align-items:center;justify-content:space-between;padding:0 8px}
.select::after{content:"";border:4px solid transparent;border-top-color:#888;margin-top:4px}
.search-btn{width:119px;height:28px;background:var(--orange);color:var(--white);font-size:10px;font-weight:700;display:flex;align-items:center;justify-content:center}
.section-title{text-align:center;font-size:27px;color:var(--ink);font-weight:400;letter-spacing:.3px}
.section-title b{font-weight:700}
.section-lead{text-align:center;font-size:12px;line-height:1.8;color:var(--muted);width:720px;margin:10px auto 0}
.for-sale{position:absolute;top:760px;left:0;width:1200px}
.duty-cards{position:absolute;top:123px;left:133px;display:flex;gap:32px}
.duty-card{width:451px;height:252px;border:1px solid var(--line);padding:18px 20px;background:var(--white)}
.icon-row{display:flex;justify-content:space-between;padding:0 3px}
.icon-row .circle{width:74px;height:74px;border-radius:50%;display:flex;align-items:center;justify-content:center}
.orange .circle{background:var(--orange)}
.blue .circle{background:var(--blue)}
.duty-head{display:flex;justify-content:space-between;align-items:center;margin-top:24px}
.duty-head h3{font-size:12px;font-weight:700;color:var(--ink)}
.duty-head .tag{font-size:9px;color:var(--white);padding:5px 10px}
.orange .tag{background:var(--blue)}
.blue .tag{background:var(--orange)}
.duty-types{display:grid;grid-template-columns:160px 96px 1fr;row-gap:8px;margin-top:18px;font-size:11px;color:#666}
.arrow{position:absolute;top:220px;width:18px;height:56px}
.by-state{position:absolute;top:1213px;left:0;width:1200px;height:467px;background:var(--band)}
.block-title{font-size:20px;color:var(--ink);font-weight:400}
.block-title b{font-weight:700}
.states{position:absolute;left:133px;top:65px}
.state-cols{display:flex;margin-top:22px}
.state-cols ul{list-style:none;width:140px}
.state-cols ul:nth-child(1){width:138px}
.state-cols ul:nth-child(2){width:149px}
.state-cols ul:nth-child(3){width:153px}
.state-cols li{font-size:11px;color:#666;text-decoration:underline;line-height:24px}
.dealer{position:absolute;left:709px;top:65px}
.dealer-box{margin-top:22px;width:358px;height:274px;border:1px solid #e0e0e0;background:var(--white);padding:20px}
.map{width:300px;height:160px;margin:0 auto;background:var(--blue);border-radius:40% 30% 45% 35%/45% 40% 50% 40%}
.dealer-foot{display:flex;justify-content:space-between;align-items:center;margin-top:28px}
.dealer-foot p{font-size:11px;color:#444;line-height:1.7;width:190px}
.dealer-foot .btn{height:28px;font-size:10px;font-weight:700}
.features{position:absolute;top:1740px;left:0;width:1200px}
.ads{position:absolute;top:117px;left:133px;display:flex;gap:28px}
.ad{width:211px;height:215px;border:1px solid #e0e0e0;padding:8px;text-align:center}
.ad .photo{height:136px}
.ad h4{font-size:12px;font-weight:400;color:var(--ink);margin-top:16px;white-space:nowrap}
.ad p{font-size:10px;color:#777;margin-top:8px}
.site-footer{position:absolute;top:2161px;left:0;width:1200px;height:271px;background:var(--band)}
.fcol{position:absolute;top:46px}
.fcol h5{font-size:12px;font-weight:700;color:var(--ink);letter-spacing:.3px}
.fcol p{font-size:11px;line-height:1.7;color:#555}
.contact-line{display:flex;align-items:center;gap:14px;margin-top:10px;font-size:16px;color:#555}
.contact-line.small{font-size:12px;margin-top:6px}
.post{margin-top:18px}
.post time{display:flex;align-items:center;gap:6px;font-size:9px;color:var(--blue);margin-top:6px}
.tweet{display:flex;gap:12px;margin-top:18px}
.tweet .dot{width:14px;height:14px;border-radius:50%;background:#3b8fd0;flex:none;margin-top:3px}
.tweet p{font-size:10px;font-style:italic;color:#777;width:230px}
.tweet p b{color:var(--blue);font-weight:400}
.tweet span{display:block;font-size:9px;color:var(--blue);font-style:normal;margin-top:4px}
.social{list-style:none;margin-top:12px}
.social li{display:flex;align-items:center;gap:12px;font-size:11px;color:#555;margin-bottom:6px}
.social li i{width:34px;height:34px;border:2px solid var(--blue-dark);border-radius:50%}
.copyright{position:absolute;top:2432px;left:0;width:1200px;height:58px;display:flex;align-items:center;justify-content:center;font-size:11px;color:#333}
</style>
</head>
<body>
<header class="site-header">
  <div class="brand">Haulway Trucks</div>
  <nav class="top-nav">
    <a>MyTrader</a><span class="sep">-</span><a>Login</a><span class="sep">-</span><a>Register</a><span class="sep">-</span><a>Find a Dealer</a><span class="sep">-</span><a>Dealer Login</a>
    <a class="btn btn-orange" style="margin-left:10px"><svg width="10" height="11" viewBox="0 0 10 11"><rect x="1" y="5" width="8" height="6" fill="#fff"/><path d="M3 5V3a2 2 0 0 1 4 0v2" stroke="#fff" fill="none" stroke-width="1.4"/></svg>Log In</a>
    <a class="btn btn-blue"><svg width="10" height="10" viewBox="0 0 10 10"><path d="M1 9l1-3 5-5 2 2-5 5z" fill="#fff"/></svg>Register</a>
    <span class="menu-toggle">MENU :<span class="ring"><svg width="16" height="12" viewBox="0 0 16 12"><path d="M0 1h16M0 6h16M0 11h16" stroke="#333" stroke-width="2"/></svg></span></span>
  </nav>
</header>

<section class="hero" role="img" aria-label="Photo of yellow semi trucks parked in a row at a warehouse loading yard under a cloudy sky">
  <div class="hero-caption">
    <h1><b>Trucks &amp;</b> Also Parts</h1>
    <p>Neque porro quisquam est, qui dolorem ipsum quia sit amet, consectetur adipisci velit...</p>
  </div>
  <div class="hero-dots"><span class="on"></span><span></span><span></span></div>
</section>

<form class="quick-search">
  <label>QUICK SEARCH :</label>
  <div class="select">SELECT A CLASS</div>
  <div class="select">SELECT A CATEGORY</div>
  <div class="select">SELECT A MAKE</div>
  <div class="select">ZIP CODE</div>
  <div class="search-btn">SEARCH</div>
</form>

<section class="for-sale">
  <h2 class="section-title"><b>TRUCKS AND</b> TRAILERS FOR SALE</h2>
  <p class="section-lead">Sed ut perspiciatis unde omnis iste natus error sit voluptatem accusantium doloremque laudantium, totam rem aperiam, eaque ipsa quae ab illo inventore veritatis et quasi architecto beatae vitae dicta...</p>
  <svg class="arrow" style="left:92px" viewBox="0 0 18 56"><path d="M16 2L2 28l14 26" fill="none" stroke="#bbb" stroke-width="1.5"/></svg>
  <svg class="arrow" style="left:1090px" viewBox="0 0 18 56"><path d="M2 2l14 26L2 54" fill="none" stroke="#bbb" stroke-width="1.5"/></svg>
  <div class="duty-cards">
    <article class="duty-card orange">
      <div class="icon-row">
        <span class="circle"><svg width="40" height="28" viewBox="0 0 40 28"><rect x="2" y="4" width="24" height="14" fill="#fff"/><path d="M26 8h7l5 6v4H26z" fill="#fff"/><circle cx="9" cy="22" r="4" fill="#fff"/><circle cx="31" cy="22" r="4" fill="#fff"/></svg></span>
        <span class="circle"><svg width="40" height="28" viewBox="0 0 40 28"><path d="M2 4h26l-4 14H4z" fill="#fff"/><path d="M28 9h6l4 5v4H26z" fill="#fff"/><circle cx="9" cy="22" r="4" fill="#fff"/><circle cx="31" cy="22" r="4" fill="#fff"/></svg></span>
        <span class="circle"><svg width="30" height="36" viewBox="0 0 30 36"><rect x="3" y="2" width="24" height="26" rx="3" fill="#fff"/><rect x="7" y="6" width="16" height="8" fill="#cc5a12"/><circle cx="8" cy="32" r="3" fill="#fff"/><circle cx="22" cy="32" r="3" fill="#fff"/></svg></span>
        <span class="circle"><svg width="40" height="28" viewBox="0 0 40 28"><rect x="2" y="2" width="24" height="16" fill="#fff"/><path d="M26 7h7l5 6v5H26z" fill="#fff"/><circle cx="9" cy="22" r="4" fill="#fff"/><circle cx="31" cy="22" r="4" fill="#fff"/></svg></span>
      </div>
      <div class="duty-head"><h3>FIND HEAVY DUTY TRUCKS FOR SALE</h3><a class="tag">SEE ALL HEAVY DUTY TRUCKS ›</a></div>
      <div class="duty-types">
        <span>Cab-Chassis</span><span>Day Cab</span><span>Conventional Sleeper Truck</span>
        <span>Flatbed-Truck</span><span>Tractor</span><span>Dump-Truck</span>
        <span>Box Truck-Straight Truck</span><span>Crane Truck</span><span>Conventional Day Cab</span>
      </div>
    </article>
    <article class="duty-card blue">
      <div class="icon-row">
        <span class="circle"><svg width="40" height="28" viewBox="0 0 40 28"><rect x="2" y="4" width="24" height="14" fill="#fff"/><path d="M26 8h7l5 6v4H26z" fill="#fff"/><circle cx="9" cy="22" r="4" fill="#fff"/><circle cx="31" cy="22" r="4" fill="#fff"/></svg></span>
        <span class="circle"><svg width="40" height="28" viewBox="0 0 40 28"><path d="M2 4h26l-4 14H4z" fill="#fff"/><path d="M28 9h6l4 5v4H26z" fill="#fff"/><circle cx="9" cy="22" r="4" fill="#fff"/><circle cx="31" cy="22" r="4" fill="#fff"/></svg></span>
        <span class="circle"><svg width="30" height="36" viewBox="0 0 30 36"><rect x="3" y="2" width="24" height="26" rx="3" fill="#fff"/><rect x="7" y="6" width="16" height="8" fill="#2d5596"/><circle cx="8" cy="32" r="3" fill="#fff"/><circle cx="22" cy="32" r="3" fill="#fff"/></svg></span>
        <span class="circle"><svg width="40" height="28" viewBox="0 0 40 28"><rect x="2" y="2" width="24" height="16" fill="#fff"/><path d="M26 7h7l5 6v5H26z" fill="#fff"/><circle cx="9" cy="22" r="4" fill="#fff"/><circle cx="31" cy="22" r="4" fill="#fff"/></svg></span>
      </div>
      <div class="duty-head"><h3>MEDIUM DUTY TRUCKS FOR SALE</h3><a class="tag">SEE ALL MEDIUM DUTY TRUCKS ›</a></div>
      <div class="duty-types">
        <span>Cab-Chassis</span><span>Day Cab</span><span>Conventional Sleeper Truck</span>
        <span>Flatbed-Truck</span><span>Tractor</span><span>Dump-Truck</span>
        <span>Box Truck-Straight Truck</span><span>Crane Truck</span><span>Conventional Day Cab</span>
      </div>
    </article>
  </div>
</section>

<section class="by-state">
  <div class="states">
    <h2 class="block-title"><b>TRUCKS FOR</b> SALE BY STATE</h2>
    <div class="state-cols">
      <ul><li>Alabama</li><li>Alaska</li><li>Arizona</li><li>Arkansas</li><li>California</li><li>Colorado</li><li>Connecticut</li><li>Delaware</li><li>Florida</li><li>Georgia</li><li>Hawaii</li><li>Idaho</li><li>Illinois</li></ul>
      <ul><li>Indiana</li><li>Iowa</li><li>Kansas</li><li>Kentucky</li><li>Lousiana</li><li>Maine</li><li>Maryland</li><li>Masachusetts</li><li>Michigan</li><li>Minnesota</li><li>Mississippi</li><li>Missouri</li><li>Montana</li></ul>
      <ul><li>Nebraska</li><li>Nevada</li><li>New Hampshire</li><li>New Jersey</li><li>New Mexico</li><li>New York</li><li>North Carolina</li><li>North Dakota</li><li>Ohio</li><li>Oklahoma</li><li>Oregon</li><li>Pennsylvania</li></ul>
      <ul><li>Rhode Island</li><li>South Carolina</li><li>South Dakota</li><li>Tennessee</li><li>Texas</li><li>Utah</li><li>Vermont</li><li>Virginia</li><li>Washington</li><li>West Virginia</li><li>Wisconsin</li><li>Wyoming</li></ul>
    </div>
  </div>
  <div class="dealer">
    <h2 class="block-title"><b>FIND A</b> DEALER</h2>
    <div class="dealer-box">
      <div class="map" role="img" aria-label="Blue map of the region with one highlighted orange area and a location pin"></div>
      <div class="dealer-foot">
        <p>Find Commercial Truck dealers by name,make and location.</p>
        <a class="btn btn-orange">FIND A DEALER</a>
      </div>
    </div>
  </div>
</section>

<section class="features">
  <h2 class="section-title"><b>FEATURE</b> ADS</h2>
  <p class="section-lead">Sed ut perspiciatis unde omnis iste natus error sit voluptatem accusantium doloremque laudantium, totam rem aperiam, eaque ipsa quae ab illo inventore veritatis et quasi architecto beatae vitae dicta...</p>
  <div class="ads">
    <article class="ad"><div class="photo" role="img" aria-label="White semi truck on a pale studio background" style="background:linear-gradient(180deg,#dfe4ea,#9aa3ad)"></div><h4>2016 Karvel Cargomax 250</h4><p>Van $29,500.00 Merrimack, NH</p></article>
    <article class="ad"><div class="photo" role="img" aria-label="White truck driving on a mountain road" style="background:linear-gradient(180deg,#6c9bd0,#8c7a62 60%,#4a4a4a)"></div><h4>2016 Karvel Cargomax 250</h4><p>Van $29,500.00 Merrimack, NH</p></article>
    <article class="ad"><div class="photo" role="img" aria-label="White van on a road through green fields" style="background:linear-gradient(180deg,#7fb2e0,#c9b87a 55%,#6c7a4a)"></div><h4>2016 Karvel Cargomax 250</h4><p>Van $29,500.00 Merrimack, NH</p></article>
    <article class="ad"><div class="photo" role="img" aria-label="Yellow van driving through a city street" style="background:linear-gradient(180deg,#5a86b8,#c8b040 55%,#4e6a8a)"></div><h4>2016 Karvel Cargomax 250</h4><p>Van $29,500.00 Merrimack, NH</p></article>
  </div>
</section>

<footer class="site-footer">
  <div class="fcol" style="left:133px">
    <h5>CONTACT INFO</h5>
    <p style="margin-top:14px">1609 # Haulway Trucks Company Name,<br>Street Name,City-446</p>
    <div class="contact-line"><svg width="16" height="16" viewBox="0 0 16 16"><path d="M3 1l3 3-2 2a10 10 0 0 0 6 6l2-2 3 3-2 2C7 15 1 9 1 3z" fill="none" stroke="#666" stroke-width="1.3"/></svg>(555) 014-2290</div>
    <div class="contact-line small"><svg width="16" height="12" viewBox="0 0 16 12"><rect x="1" y="1" width="14" height="10" fill="none" stroke="#666" stroke-width="1.3"/><path d="M1 1l7 6 7-6" fill="none" stroke="#666" stroke-width="1.3"/></svg>info@haulway.example</div>
  </div>
  <div class="fcol" style="left:379px;width:240px">
    <h5>RECENT BLOG</h5>
    <div class="post"><p>Neque porro quisquam est, qui dolorem ipsum quia dolor sit</p><time><svg width="9" height="9" viewBox="0 0 9 9"><circle cx="4.5" cy="4.5" r="3.8" fill="none" stroke="#2d5596"/><path d="M4.5 2.5v2h1.5" stroke="#2d5596" fill="none"/></svg>Posted On 23 Nov 2016</time></div>
    <div class="post"><p>Neque porro quisquam est, qui dolorem ipsum quia dolor sit</p><time><svg width="9" height="9" viewBox="0 0 9 9"><circle cx="4.5" cy="4.5" r="3.8" fill="none" stroke="#2d5596"/><path d="M4.5 2.5v2h1.5" stroke="#2d5596" fill="none"/></svg>Posted On 23 Nov 2016</time></div>
  </div>
  <div class="fcol" style="left:655px">
    <h5>CHIRP FEED</h5>
    <div class="tweet"><i class="dot"></i><p><b>@haulway</b> is a long established fact that a reader will be distracted by the ...<span>2 month ago</span></p></div>
    <div class="tweet"><i class="dot"></i><p><b>@haulway</b> is a long established fact that a reader will be distracted by the ...<span>2 month ago</span></p></div>
  </div>
  <div class="fcol" style="left:969px">
    <h5>FOLLOW &nbsp;US</h5>
    <ul class="social"><li><i></i>FriendHub</li><li><i></i>ChirpNet</li><li><i></i>CirclePlus</li><li><i></i>WorkLink</li></ul>
  </div>
</footer>
<div class="copyright">Copyrights © 2016 . Haulway Trucks | Allrights Reserved.</div>
</body>
</html>
```